BQL Groundworks & Freight Business Card

Can you please design a business card for an Earthworks, Haulage truck and machinery hire company. They also provide sand soil and mulch supply, as well as screening of products. Can you re-create the logo from the attached but add BQL Groundworks & Freight just use the three diamond design.

Target Market(s)

Earthmoving and Transport, Landscapers, Construction

Contact Information for Business Card

ABN 52 907 334 816, Doug Pelham, Managing Director, BQL Groundworks & Freight Mobile 0438 256 904 Email bqlfreight2010@mailvane.net

Font styles to use
Sans Serif

Colors
ec1f27
000000
cbcbcb
ffffff

Requirements
Must have
• Listed on the back, Earthworks | Haulage | Truck and Machinery Hire | Sand, Soil & Mulch Supply | Screening of Products
Nice to have
• Would be good for it to look appealing to a mans man, because it relates to heavy machinery, earthworks, construction etc. Black, red and white would be good maybe with a bit of silver somewhere.
Should not have
• not sure

```html
<!DOCTYPE html>
<html lang="en">
<head>
<meta charset="UTF-8">
<title>BQL Groundworks &amp; Freight Business Card</title>
<link href="https://fonts.googleapis.com/css2?family=Montserrat:wght@400;500;700;800&display=swap" rel="stylesheet">
<style>
  :root {
    --red: #ec1f27;
    --black: #000000;
    --ink: #111112;
    --silver: #cbcbcb;
    --paper: #e9e9e9;
    --white: #ffffff;
    --stage: #2a2a2c;
  }
  * { box-sizing: border-box; margin: 0; padding: 0; }
  html, body { width: 1200px; height: 660px; overflow: hidden; }
  body {
    background: var(--stage);
    font-family: "Montserrat", Arial, sans-serif;
    position: relative;
  }
  .card {
    position: absolute;
    width: 520px;
    height: 297px;
    overflow: hidden;
    box-shadow: 0 14px 30px rgba(0,0,0,.55);
    background: var(--ink);
  }
  .card--front { left: 50px; top: 182px; }
  .card--back { left: 630px; top: 182px; }

  /* Front */
  .band-dark { position: absolute; left: 0; right: 0; background: linear-gradient(180deg, #1c1c1e, #050505); }
  .band-dark--top { top: 0; height: 74px; }
  .band-dark--bottom { top: 188px; bottom: 0; }
  .rule-red { position: absolute; left: 0; right: 0; height: 3px; background: var(--red); }
  .band-light {
    position: absolute; left: 0; right: 0; top: 80px; height: 102px;
    background: linear-gradient(180deg, #f1f1f1, var(--paper));
    display: flex; align-items: center; justify-content: center;
  }

  /* Brand lockup */
  .brand { display: flex; align-items: center; gap: 12px; }
  .brand__mark { width: 30px; height: 30px; background: var(--red); flex: none; }
  .brand__name {
    font-weight: 800; color: var(--black); text-transform: uppercase;
    line-height: 1.05; font-size: 22px; letter-spacing: .5px;
  }
  .brand__name span { display: block; font-size: 13px; letter-spacing: 2.2px; }

  /* Back */
  .back__top {
    position: absolute; left: 0; right: 0; top: 0; height: 130px;
    background: linear-gradient(180deg, #f1f1f1, var(--paper));
    display: flex; align-items: center; justify-content: center;
  }
  .back__body {
    position: absolute; left: 0; right: 0; top: 130px; bottom: 22px;
    background: linear-gradient(180deg, #1b1b1d, #060606);
  }
  .back__foot { position: absolute; left: 0; right: 0; bottom: 0; height: 22px; background: var(--red); }
  .back__body .rule-red { top: 0; height: 2px; }

  .contact { position: absolute; left: 26px; top: 22px; color: var(--white); }
  .contact__name { font-weight: 700; font-size: 16px; text-transform: uppercase; letter-spacing: .5px; }
  .contact__role { color: var(--red); font-size: 12.5px; font-weight: 500; margin-bottom: 10px; }
  .contact__line { display: flex; align-items: center; gap: 8px; font-size: 11.5px; margin-top: 5px; }
  .contact__line svg { width: 12px; height: 12px; flex: none; }
  .contact__abn { font-size: 11.5px; margin-top: 7px; }

  .divider { position: absolute; left: 290px; top: 14px; bottom: 14px; width: 2px; background: var(--red); }

  .services { position: absolute; left: 308px; top: 18px; list-style: none; }
  .services li {
    color: var(--red); font-size: 12px; font-weight: 500; margin-bottom: 6px;
    display: flex; align-items: center; gap: 8px;
  }
  .services li::before {
    content: ""; width: 6px; height: 6px; background: var(--silver);
    transform: rotate(45deg); flex: none;
  }
</style>
</head>
<body>

<section class="card card--front" aria-label="Business card front">
  <div class="band-dark band-dark--top"></div>
  <div class="rule-red" style="top:74px"></div>
  <div class="band-light">
    <div class="brand">
      <div class="brand__mark"></div>
      <div class="brand__name">BQL Groundworks<span>&amp; Freight</span></div>
    </div>
  </div>
  <div class="rule-red" style="top:182px"></div>
  <div class="band-dark band-dark--bottom"></div>
</section>

<section class="card card--back" aria-label="Business card back">
  <div class="back__top">
    <div class="brand">
      <div class="brand__mark"></div>
      <div class="brand__name">BQL Groundworks<span>&amp; Freight</span></div>
    </div>
  </div>
  <div class="back__body">
    <div class="rule-red"></div>
    <div class="contact">
      <p class="contact__name">Doug Pelham</p>
      <p class="contact__role">Managing Director</p>
      <p class="contact__line">
        <svg viewBox="0 0 12 12" aria-hidden="true"><rect x="3" y="0.8" width="6" height="10.4" rx="1" fill="none" stroke="#ec1f27" stroke-width="1.3"/><circle cx="6" cy="9.3" r=".7" fill="#ec1f27"/></svg>
        0438 256 904
      </p>
      <p class="contact__line">
        <svg viewBox="0 0 12 12" aria-hidden="true"><rect x="0.5" y="2" width="11" height="8" fill="#ec1f27"/><path d="M0.8 2.4 6 6.6l5.2-4.2" fill="none" stroke="#111" stroke-width="1"/></svg>
        bqlfreight2010@mailvane.net
      </p>
      <p class="contact__abn">ABN 52 907 334 816</p>
    </div>
    <div class="divider"></div>
    <ul class="services">
      <li>Earthworks</li>
      <li>Haulage</li>
      <li>Truck and Machinery Hire</li>
      <li>Sand, Soil &amp; Mulch Supply</li>
      <li>Screening of Products</li>
    </ul>
  </div>
  <div class="back__foot"></div>
</section>

</body>
</html>
```